Breakfast Cafe - The Sunny Perch

It is for my breakfast and lunch cafe with a hawaiian / beach theme. I am open 7 days a week from 7am to 2pm. We serve traditional American food such as omelettes, pancakes, burgers and sandwiches. I'll upload my old card and my new logo to be used. We have a lot of day to day regulars who eat there during the week, our t-shirts actually say 'Locals Only' on them. Hope this helps. Thanks.

Target Market(s)

anyone who has an appetite!

Industry/Entity Type

American Restaurant

Contact Information for Business Card

7340D Marlin Harbor Road
Long Beach, California
(555) 317-2286

Requirements
Must have
• Address and phone number easily readable.
Nice to have
• beach or tropical theme

```html
<!DOCTYPE html>
<html lang="en">
<head>
<meta charset="utf-8">
<title>The Sunny Perch – Business Card</title>
<link href="https://fonts.googleapis.com/css2?family=Questrial&display=swap" rel="stylesheet">
<style>
  :root {
    --page-bg: #f5f5f5;
    --sky: #2f5e9e;
    --cloud: #8fa9c8;
    --sea: #2e9a8c;
    --sea-deep: #2a7f74;
    --sand: #b9a57c;
    --shade: rgba(20, 40, 70, 0.28);
    --brand-blue: #6cc9e6;
    --brand-orange: #c27a30;
    --band: #bf7630;
    --white: #ffffff;
  }
  * { box-sizing: border-box; margin: 0; padding: 0; }
  html, body { width: 1200px; height: 1198px; overflow: hidden; }
  body {
    background: var(--page-bg);
    font-family: "Questrial", "Century Gothic", sans-serif;
    position: relative;
  }
  .card {
    position: absolute;
    top: 261px;
    width: 387px;
    height: 644px;
    overflow: hidden;
  }
  .card--front { left: 139px; }
  .card--back { left: 658px; }
  .card__photo {
    position: absolute;
    inset: 0;
    background:
      linear-gradient(180deg, var(--sky) 0%, var(--cloud) 32%, var(--sky) 48%, var(--sea) 62%, var(--sea-deep) 85%, var(--sand) 100%);
  }
  .card__photo::after {
    content: "";
    position: absolute;
    inset: 0;
    background: var(--shade);
  }
  .brand {
    position: absolute;
    left: 0;
    right: 0;
    text-align: center;
  }
  .brand__name {
    color: var(--brand-blue);
    font-size: 40px;
    line-height: 1;
    letter-spacing: 0.5px;
  }
  .brand__place {
    color: var(--brand-orange);
    font-size: 12px;
    letter-spacing: 5px;
    margin-top: 12px;
  }
  .card--front .brand { top: 386px; }
  .card--back .brand { top: 236px; }
  .card--back .brand__name { font-size: 33px; }
  .card--back .brand__place { font-size: 10px; letter-spacing: 4px; margin-top: 10px; }
  .contact {
    position: absolute;
    left: 56px;
    top: 342px;
    color: var(--white);
    font-size: 16px;
    line-height: 22px;
  }
  .contact__row { display: flex; align-items: flex-start; gap: 11px; margin-bottom: 8px; }
  .contact__icon { width: 22px; height: 22px; flex: none; }
  .hours {
    position: absolute;
    left: 56px;
    top: 436px;
    color: var(--white);
    font-size: 21px;
    line-height: 29px;
  }
  .hours__title { font-weight: 700; letter-spacing: 0.5px; }
  .band {
    position: absolute;
    left: 0;
    right: 0;
    background: var(--band);
  }
  .band--thin { top: 534px; height: 21px; }
  .band--wide { top: 573px; height: 71px; }
</style>
</head>
<body>
  <section class="card card--front">
    <div class="card__photo" role="img" aria-label="Tropical beach photo with palm tree, blue sky and turquoise sea"></div>
    <div class="brand">
      <div class="brand__name">The Sunny Perch</div>
      <div class="brand__place">LONG BEACH, CA</div>
    </div>
  </section>

  <section class="card card--back">
    <div class="card__photo" role="img" aria-label="Tropical beach photo with palm tree, blue sky and turquoise sea"></div>
    <div class="brand">
      <div class="brand__name">The Sunny Perch</div>
      <div class="brand__place">LONG BEACH, CA</div>
    </div>
    <div class="contact">
      <div class="contact__row">
        <svg class="contact__icon" viewBox="0 0 24 24" aria-hidden="true">
          <circle cx="12" cy="12" r="12" fill="#fff"/>
          <path d="M12 5a4.5 4.5 0 0 0-4.5 4.5c0 3.4 4.5 8.5 4.5 8.5s4.5-5.1 4.5-8.5A4.5 4.5 0 0 0 12 5z" fill="none" stroke="#2e7f8a" stroke-width="1.6"/>
          <circle cx="12" cy="9.5" r="1.7" fill="#2e7f8a"/>
        </svg>
        <div>7340D Marlin Harbor Road<br>Long Beach, California</div>
      </div>
      <div class="contact__row">
        <svg class="contact__icon" viewBox="0 0 24 24" aria-hidden="true">
          <circle cx="12" cy="12" r="12" fill="#fff"/>
          <path d="M8.2 6.2l2 2.4c.3.4.3.9 0 1.3l-.9 1c.8 1.6 2 2.8 3.6 3.6l1-.9c.4-.3.9-.3 1.3 0l2.4 2c.4.3.4.9.1 1.3l-1 1.1c-.6.6-1.5.8-2.3.5-3.6-1.4-6.4-4.2-7.8-7.8-.3-.8-.1-1.7.5-2.3l1.1-1c.4-.3 1-.3 1.3.1z" fill="#2e7f8a"/>
        </svg>
        <div>(555) 317-2286</div>
      </div>
    </div>
    <div class="hours">
      <div class="hours__title">BREAKFAST AND LUNCH</div>
      <div>7am-2pm daily</div>
    </div>
    <div class="band band--thin"></div>
    <div class="band band--wide"></div>
  </section>
</body>
</html>
```